Stationary KV Relay
business card, letterhead, envelopes, email signature,memo pad and invoice/quotes
Project: Stationary KV Relay
Stationary KV Relay   - Telecommunications
Creative Brief
Use same font as used in my logo
or any
Bright & Fun-filled
Tom Variscoff
CEO
3F B28 GALERI NUSAPARK JAKARTA PUSAT 14071
tom@kvrelay.com
www.kvrelay.com
Feel free to utilize different styles but try to stick to the company logo colors as best as possible.
Require: Business card, Stationary, Envelopes, Invoice, E-mail signature & Notepad
pwarnet pwarnet
EPS format upload already
brightoak brightoak
definitely!! but there is lots of designs please rate my design so i will easy to make the stationary of your like designs thanks :)
Business card, Stationary, Envelopes, Invoice, E-mail signature & Notepad
Check your private massage! thanks!
nice for this time

```html
<!DOCTYPE html>
<html lang="en">
<head>
<meta charset="utf-8">
<title>KV Relay – Business Card</title>
<link href="https://fonts.googleapis.com/css2?family=Questrial&family=Montserrat:wght@700&display=swap" rel="stylesheet">
<style>
  :root {
    --backdrop: #e6e7ea;
    --card: #ffffff;
    --brand-blue: #1b5fae;
    --brand-orange: #f39a1e;
    --ink-blue: #1f4f93;
    --ink-grey: #4a4f59;
    --icon-blue: #2f6fc0;
  }
  * { box-sizing: border-box; margin: 0; padding: 0; }
  html, body {
    width: 1200px; height: 900px; overflow: hidden;
    background: var(--backdrop);
  }
  .canvas {
    width: 1200px; height: 900px;
    display: flex; align-items: center; justify-content: center;
  }
  .business-card {
    position: relative;
    width: 1000px; height: 570px;
    background: var(--card);
    box-shadow: 0 10px 30px rgba(0,0,0,0.12);
    font-family: "Questrial", sans-serif;
    font-variant: small-caps;
  }
  .brand {
    position: absolute; left: 200px; top: 150px;
    display: flex; align-items: center; gap: 18px;
  }
  .brand-dot {
    width: 74px; height: 74px; border-radius: 50%;
    background: var(--brand-orange);
  }
  .brand-name {
    font-family: "Montserrat", sans-serif;
    font-weight: 700; font-size: 64px; letter-spacing: 1px;
    color: var(--brand-blue); text-transform: uppercase;
    font-variant: normal;
  }
  .holder {
    position: absolute; left: 400px; top: 330px;
    font-size: 30px; letter-spacing: 1.5px; color: var(--ink-blue);
  }
  .holder .divider { color: var(--ink-grey); margin: 0 10px; }
  .holder .role { color: var(--ink-grey); }
  .contacts {
    position: absolute; left: 70px; right: 60px; top: 418px;
    display: grid; grid-template-columns: auto auto; column-gap: 26px; row-gap: 10px;
    justify-content: space-between;
    font-size: 21px; letter-spacing: 1.6px; color: var(--ink-grey);
  }
  .contact { display: flex; align-items: center; gap: 8px; white-space: nowrap; }
  .contact-pair { display: flex; gap: 22px; }
  .icon { width: 22px; height: 22px; flex: none; }
</style>
</head>
<body>
<main class="canvas">
  <article class="business-card">
    <div class="brand">
      <span class="brand-dot"></span>
      <span class="brand-name">KV Relay</span>
    </div>

    <p class="holder"><span class="name">Tom Variscoff</span><span class="divider">|</span><span class="role">CEO</span></p>

    <div class="contacts">
      <p class="contact">
        <svg class="icon" viewBox="0 0 22 22"><circle cx="11" cy="11" r="11" fill="var(--icon-blue)"/><path d="M11 5a4 4 0 0 0-4 4c0 3 4 8 4 8s4-5 4-8a4 4 0 0 0-4-4zm0 5.5a1.5 1.5 0 1 1 0-3 1.5 1.5 0 0 1 0 3z" fill="#fff"/></svg>
        3F B28 Galeri Nusapark Jakarta Pusat 14071
      </p>
      <p class="contact">
        <svg class="icon" viewBox="0 0 22 22"><circle cx="11" cy="11" r="11" fill="var(--icon-blue)"/><circle cx="11" cy="11" r="5.5" fill="none" stroke="#fff" stroke-width="1.3"/><path d="M5.5 11h11M11 5.5c-2.5 3-2.5 8 0 11M11 5.5c2.5 3 2.5 8 0 11" fill="none" stroke="#fff" stroke-width="1.1"/></svg>
        www.kvrelay.com
      </p>
      <div class="contact-pair">
        <p class="contact">
          <svg class="icon" viewBox="0 0 22 22"><circle cx="11" cy="11" r="11" fill="var(--icon-blue)"/><path d="M7.5 6l2 0 1 2.6-1.3 1a6 6 0 0 0 2.7 2.7l1-1.3 2.6 1v2c0 .6-.5 1-1 1A8.5 8.5 0 0 1 6.5 7c0-.5.4-1 1-1z" fill="#fff"/></svg>
          +622-140-555-218
        </p>
        <p class="contact">
          <svg class="icon" viewBox="0 0 22 22"><circle cx="11" cy="11" r="11" fill="var(--icon-blue)"/><rect x="8" y="5" width="6" height="12" rx="1" fill="#fff"/><rect x="9" y="6.5" width="4" height="7" fill="var(--icon-blue)"/></svg>
          +628-553-710-464
        </p>
      </div>
      <p class="contact">
        <svg class="icon" viewBox="0 0 22 22"><circle cx="11" cy="11" r="11" fill="var(--icon-blue)"/><rect x="5.5" y="7" width="11" height="8" rx="1" fill="#fff"/><path d="M5.5 7.5l5.5 4 5.5-4" fill="none" stroke="var(--icon-blue)" stroke-width="1.1"/></svg>
        tom@kvrelay.com
      </p>
    </div>
  </article>
</main>
</body>
</html>
```